Flyer-Design für Autolackiererei
Hallo es muss nur noch die Richtige Telefonnumer rein , die bekomm ich esrt von Fernolux zu geschickt
Zielgruppe
Karosserie & Autolackiererei
Autohäuser , Privatkunden , Bussunterhemen , LKW Unterhemen , Versicherungen
Aufgabenstellung
Neueröffung Von Autolackiererei ab 01.03.2019 bitte ganz wichtig muss auf flayer drauf.
Unfallinstansetztung , Fahrzeuglackierung Jeglicher Art , Oldtimer Restauration , Fahrzeugaufbereitung , Achsvermessung ,Felgen Lackieren ,Hagelschaden ,
inspektionen alle Fahrzeug Fabrikaten, Vexa, Reifenservice
Hol und Bring service ,scheibenaustausch abwicklung mit versicherung ,
Smart Repair

```html
<!DOCTYPE html>
<html lang="de">
<head>
<meta charset="utf-8">
<title>Flyer Autolackiererei Keller</title>
<link rel="stylesheet" href="https://fonts.googleapis.com/css2?family=Bebas+Neue&family=Didact+Gothic&display=swap">
<style>
  :root {
    --blue: #2699d8;
    --blue-deep: #1a6fa3;
    --dark: #2b2f33;
    --white: #ffffff;
    --text-grey: #6a6e72;
    --page: #ffffff;
  }
  * { margin: 0; padding: 0; box-sizing: border-box; }
  html, body { width: 686px; height: 1200px; overflow: hidden; background: var(--page); }
  .canvas {
    position: relative; width: 686px; height: 1200px;
    display: flex; justify-content: center; align-items: center; gap: 30px;
  }
  .flyer {
    position: relative; width: 300px; height: 600px; overflow: hidden;
    background: var(--white);
    box-shadow: 0 8px 28px rgba(0,0,0,.28);
    font-family: "Bebas Neue", sans-serif;
    font-weight: 400;
  }
  .flyer-shapes { position: absolute; inset: 0; }
  .brand-mark {
    position: absolute; left: 86px; top: 70px; width: 134px; height: 134px;
    display: flex; align-items: center; justify-content: center; text-align: center;
    border: 4px solid var(--blue); border-radius: 50%;
    color: var(--white); font-size: 21px; line-height: 1.05; letter-spacing: .5px;
  }
  .opening {
    position: absolute; left: 32px; width: 239px; top: 296px; height: 100px;
    display: flex; flex-direction: column; justify-content: flex-end;
    text-align: center; color: var(--white); line-height: .95;
  }
  .opening-label { font-size: 44px; }
  .opening-date { font-size: 58px; }
  .trade {
    position: absolute; left: 32px; width: 239px; top: 428px;
    text-align: center; color: var(--blue); font-size: 40px; line-height: .92;
    font-weight: 400;
  }
  .trade-note { display: block; font-size: 16px; margin-top: 8px; line-height: 1; }
  .name-band {
    position: absolute; left: 32px; width: 239px; top: 545px; height: 55px;
    display: flex; align-items: center; justify-content: center;
    color: var(--white); font-size: 24px;
  }
  .services-title {
    position: absolute; left: 48px; top: 24px;
    color: var(--white); font-size: 57px; line-height: 1.03; font-weight: 400;
  }
  .service-list {
    position: absolute; left: 38px; top: 194px; list-style: none;
    font-family: "Didact Gothic", sans-serif; font-size: 14.5px; line-height: 20.2px;
    color: var(--text-grey); white-space: nowrap;
  }
  .service-list li { position: relative; padding-left: 10px; }
  .service-list li::before {
    content: "»"; position: absolute; left: 0; top: -1px;
    color: var(--blue); font-weight: bold; font-size: 13px;
  }
  .contact-box {
    position: absolute; left: 32px; width: 239px; top: 511px; height: 89px;
    background: var(--blue); color: var(--white); padding: 9px 0 0 16px;
    font-style: normal;
  }
  .contact-name { font-size: 16px; margin-bottom: 4px; }
  .contact-line { display: flex; align-items: center; gap: 7px; font-size: 11.5px; height: 17px; }
  .contact-icon { width: 11px; height: 11px; flex: none; }
</style>
</head>
<body>
<main class="canvas">

  <section class="flyer flyer-front">
    <svg class="flyer-shapes" viewBox="0 0 300 600" width="300" height="600">
      <defs>
        <linearGradient id="front-photo" x1="0" y1="0" x2="1" y2="1">
          <stop offset="0" stop-color="#3a9fd6"/>
          <stop offset=".55" stop-color="#1f5f86"/>
          <stop offset="1" stop-color="#2c80b5"/>
        </linearGradient>
      </defs>
      <rect role="img" aria-label="Foto: Scheinwerfer eines blauen Autos" x="0" y="0" width="300" height="335" fill="url(#front-photo)"/>
      <rect x="32" y="0" width="239" height="335" fill="var(--dark)"/>
      <polygon points="0,227 300,322 300,600 0,600" fill="var(--white)"/>
      <polygon points="32,222 271,297 271,404 32,404" fill="var(--blue)"/>
      <rect x="32" y="545" width="239" height="55" fill="var(--blue)"/>
    </svg>
    <div class="brand-mark">Autolackiererei<br>Keller</div>
    <div class="opening">
      <div class="opening-label">Neueröffnung</div>
      <div class="opening-date">01.03.2019</div>
    </div>
    <h1 class="trade">Karosserie und<br>Autolackiererei<span class="trade-note">-Meisterbetrieb-</span></h1>
    <div class="name-band">Autolackiererei Keller</div>
  </section>

  <section class="flyer flyer-back">
    <svg class="flyer-shapes" viewBox="0 0 300 600" width="300" height="600">
      <defs>
        <linearGradient id="back-photo" x1="0" y1="0" x2="1" y2="1">
          <stop offset="0" stop-color="#3a9fd6"/>
          <stop offset=".55" stop-color="#1f5f86"/>
          <stop offset="1" stop-color="#2c80b5"/>
        </linearGradient>
      </defs>
      <rect role="img" aria-label="Foto: Scheinwerfer eines blauen Autos" x="0" y="0" width="300" height="240" fill="url(#back-photo)"/>
      <rect x="32" y="0" width="239" height="211" fill="var(--dark)"/>
      <polygon points="0,160 300,238 300,600 0,600" fill="var(--white)"/>
    </svg>
    <h2 class="services-title">Unsere<br>Leistungen</h2>
    <ul class="service-list">
      <li>Vexa</li>
      <li>Smart Repair</li>
      <li>Reifenservice</li>
      <li>Hagelschaden</li>
      <li>Felgen lackieren</li>
      <li>Achsvermessung</li>
      <li>Unfallinstansetztung</li>
      <li>Hol- und Bringservice</li>
      <li>Oldtimer Restauration</li>
      <li>Fahrzeugaufbereitung</li>
      <li>Fahrzeuglackierung (jeglicher Art)</li>
      <li>Inspektionen aller Fahrzeug<br>Fabrikaten</li>
      <li>Scheibenaustausch<br>(inkl. Abwicklung mit Versicherung)</li>
    </ul>
    <address class="contact-box">
      <div class="contact-name">Autolackiererei Keller</div>
      <div class="contact-line">
        <svg class="contact-icon" viewBox="0 0 12 12"><rect width="12" height="12" fill="#fff"/><path d="M6 2.5 2.5 5.5H3.7V9.5H8.3V5.5H9.5Z" fill="var(--blue)"/></svg>
        Werkstraße 7, 72999 Lindenau
      </div>
      <div class="contact-line">
        <svg class="contact-icon" viewBox="0 0 12 12"><rect width="12" height="12" fill="#fff"/><rect x="2.5" y="3.5" width="7" height="5" fill="none" stroke="var(--blue)"/><path d="M2.5 3.5 6 6.3 9.5 3.5" fill="none" stroke="var(--blue)"/></svg>
        info@autolack-keller.de
      </div>
      <div class="contact-line">
        <svg class="contact-icon" viewBox="0 0 12 12"><rect width="12" height="12" fill="#fff"/><circle cx="6" cy="6" r="3.5" fill="none" stroke="var(--blue)"/><path d="M2.5 6H9.5M6 2.5C4.5 4.5 4.5 7.5 6 9.5M6 2.5C7.5 4.5 7.5 7.5 6 9.5" fill="none" stroke="var(--blue)" stroke-width=".7"/></svg>
        autolack-keller.de
      </div>
    </address>
  </section>

</main>
</body>
</html>
```